Quote Cards With TK May 2025 for Instagram

I would like to put these quotes over one of the pictures attached; Instagram (new size: 4:5 (1080 x 1350 pixels) One Quote per picture, and I want the quote to be bold or easy to read as well. I provided a few reference graphics that I really like as examples below. In very small letters at the bottom add @TKBarlowOnline

All of the pictures are attached; you can pick any photo and add one quote to it; but no stock photography

```html
<!DOCTYPE html>
<html lang="en">
<head>
<meta charset="utf-8">
<title>Quote Cards With TK</title>
<link rel="stylesheet" href="https://fonts.googleapis.com/css2?family=Oswald:wght@500;700&family=Montserrat:wght@600;800;900&family=Lobster&family=Great+Vibes&family=Playfair+Display:ital,wght@1,800&display=swap">
<style>
:root{
  --bg:#dcdcdc;
  --pink:#f7077f;
  --pink-soft:#ff3a9c;
  --yellow:#ffe500;
  --white:#ffffff;
  --ink:#0a0a0a;
}
*{margin:0;padding:0;box-sizing:border-box}
html,body{width:1200px;height:785px;overflow:hidden;background:var(--bg)}
.board{position:relative;width:1200px;height:785px}
.card{position:absolute;width:248px;height:310px;overflow:hidden;background:var(--white)}
.card > *{position:absolute}
.pink{background:radial-gradient(ellipse at 20% 110%,var(--pink-soft) 0%,var(--pink) 55%)}
.line{left:0;right:0;text-align:center;white-space:nowrap;line-height:1}
.cond{font-family:'Oswald',sans-serif;font-weight:700;letter-spacing:-.5px}
.heavy{font-family:'Montserrat',sans-serif;font-weight:800}
.script{font-family:'Great Vibes',cursive;color:var(--white)}
.handle{font-family:'Montserrat',sans-serif;font-weight:600;font-size:7.5px;line-height:1}
.frame{border:1.5px solid var(--ink)}
.photo{background:linear-gradient(160deg,#3a2030 0%,#7a2a55 55%,#c0306f 100%);border-radius:40% 40% 0 0}
.c-white{color:var(--white)}
.c-yellow{color:var(--yellow)}
.c-pink{color:var(--pink)}
.c-ink{color:var(--ink)}
.shadow-ink{text-shadow:2px 2px 0 var(--ink)}
</style>
</head>
<body>
<main class="board">

  <!-- Card 1 -->
  <section class="card" style="left:73px;top:71px">
    <div class="frame" style="left:11px;top:10px;width:227px;height:140px"></div>
    <div class="pink" style="left:0;top:143px;width:248px;height:167px"></div>
    <div class="line heavy c-pink shadow-ink" style="top:17px;font-size:38px;font-weight:900">TIRED</div>
    <div class="line heavy c-pink shadow-ink" style="top:59px;font-size:40px;font-weight:900">MOODY</div>
    <div class="line heavy c-ink" style="top:104px;font-size:29px;font-weight:900;text-shadow:2px 2px 0 var(--pink)">STUBBORN</div>
    <div class="line c-white shadow-ink" style="top:148px;font-family:'Lobster',cursive;font-size:44px">Belly Fat</div>
    <div class="line script" style="top:205px;font-size:24px">Your hormones are</div>
    <div class="line script" style="top:233px;font-size:24px">screaming for help</div>
    <div class="heavy c-ink" style="left:73px;top:265px;width:101px;height:18px;background:var(--white);font-size:9.5px;line-height:18px;text-align:center">LET'S FIX THAT</div>
    <div class="line handle c-white" style="top:290px">@TKBarlowOnline</div>
  </section>

  <!-- Card 2 -->
  <section class="card" style="left:343px;top:71px">
    <div class="pink" style="left:0;top:0;width:248px;height:234px"></div>
    <div class="frame" style="left:11px;top:234px;width:227px;height:63px;border-top:none"></div>
    <div class="line cond c-white" style="top:18px;font-size:32px">THAT STUBBORN</div>
    <svg style="left:20px;top:62px" width="208" height="34" viewBox="0 0 208 34" aria-hidden="true">
      <g fill="#ffe500"><rect x="0" y="12" width="4" height="10"/><rect x="6" y="4" width="8" height="26"/><rect x="14" y="14" width="6" height="6"/>
      <rect x="188" y="14" width="6" height="6"/><rect x="194" y="4" width="8" height="26"/><rect x="204" y="12" width="4" height="10"/></g>
    </svg>
    <div class="line cond c-yellow shadow-ink" style="top:58px;font-size:38px">WEIGHT?</div>
    <div style="left:10px;top:116px;width:228px;height:32px;background:var(--white);transform:skewY(-2deg)"></div>
    <div class="line cond c-pink" style="top:116px;font-size:23px">IT'S NOT YOUR FAULT</div>
    <div class="line c-white" style="top:166px;font-family:'Oswald',sans-serif;font-style:italic;font-weight:500;font-size:14px">YOUR HORMONES ARE TO</div>
    <div class="line c-white" style="top:189px;font-family:'Oswald',sans-serif;font-style:italic;font-weight:500;font-size:14px">BLAME AND YOU'RE NOT ALONE</div>
    <div class="line heavy c-ink" style="top:244px;font-size:20px">BUT THERE IS A FIX</div>
    <div class="line handle c-ink" style="top:280px">@TKBarlowOnline</div>
  </section>

  <!-- Card 3 -->
  <section class="card" style="left:614px;top:71px">
    <div class="pink" style="left:0;top:0;width:248px;height:203px"></div>
    <div class="frame" style="left:11px;top:203px;width:226px;height:96px;border-top:none"></div>
    <div class="line heavy c-white" style="top:20px;font-size:25px;font-weight:900">YOUR BELLY IS</div>
    <div class="line heavy c-white" style="top:50px;font-size:34px;font-weight:900">NOT FAT...</div>
    <div style="left:15px;top:103px;width:216px;height:30px;background:var(--white);border-radius:4px"></div>
    <div class="line c-pink" style="top:101px;font-family:'Playfair Display',serif;font-style:italic;font-weight:800;font-size:28px">it's hormonal</div>
    <div class="line heavy c-white" style="top:150px;font-size:17px">AND HERE'S HOW TO</div>
    <div class="line heavy c-white" style="top:170px;font-size:17px">FIX IT</div>
    <div class="line heavy c-ink" style="top:209px;font-size:14px">COMMENT</div>
    <div style="left:49px;top:226px;width:151px;height:25px;background:var(--pink);border-radius:7px"></div>
    <div class="line heavy c-white" style="top:230px;font-size:18px">HORMONES</div>
    <div class="line heavy c-ink" style="top:259px;font-size:15px">IF NOTHING IS WORKING</div>
    <div class="line handle c-ink" style="top:285px">@TKBarlowOnline</div>
  </section>

  <!-- Card 4 -->
  <section class="card" style="left:884px;top:71px">
    <div class="pink" style="left:0;top:0;width:248px;height:237px"></div>
    <div style="left:14px;top:13px;width:220px;height:105px;border-left:2px solid var(--white);border-top:2px solid var(--white);border-right:2px solid var(--white)"></div>
    <div class="frame" style="left:16px;top:237px;width:217px;height:58px;border-top:none"></div>
    <div class="cond c-white" style="left:33px;top:24px;font-size:23px;line-height:1">THE STUBBORN</div>
    <div class="cond c-yellow shadow-ink" style="left:32px;top:46px;font-size:47px;line-height:1">BELLY FAT</div>
    <div class="cond c-white" style="left:33px;top:95px;font-size:23px;line-height:1;padding-right:6px;background:var(--pink)">AFTER 40?</div>
    <div class="line cond c-white" style="top:130px;font-size:19px">IT'S <span class="c-yellow">NOT</span> ABOUT</div>
    <div class="line cond c-white" style="top:153px;font-size:19px">CALORIES</div>
    <div class="line heavy c-white" style="top:187px;font-size:17px">IT'S ABOUT YOUR</div>
    <div class="line heavy c-white" style="top:207px;font-size:17px">HORMONES</div>
    <div class="line heavy c-ink" style="top:244px;font-size:20px">HERE IS THE FIX!</div>
    <div class="line handle c-ink" style="top:281px">@TKBarlowOnline</div>
  </section>

  <!-- Card 5 -->
  <section class="card" style="left:73px;top:403px">
    <div class="pink" style="left:0;top:0;width:248px;height:239px"></div>
    <div class="photo" role="img" aria-label="Photo of TK in a sheer black top, looking over her shoulder" style="left:150px;top:53px;width:98px;height:186px"></div>
    <div class="cond c-white" style="left:11px;top:16px;font-size:35px;line-height:1">TIRED. MOODY.</div>
    <div class="cond c-white" style="left:11px;top:57px;font-size:33px;line-height:1">STUBBORN</div>
    <div class="cond c-yellow" style="left:11px;top:95px;font-size:35px;line-height:1">BELLY FAT.</div>
    <div style="left:0;top:131px;width:151px;height:2px;background:var(--yellow)"></div>
    <div class="cond c-white" style="left:11px;top:158px;font-size:22px;line-height:1.13">Your hormones<br>are screaming<br>for help!</div>
    <div class="heavy c-ink" style="left:11px;top:246px;font-size:26px;line-height:1;white-space:nowrap">LET'S FIX THAT</div>
    <div class="handle c-ink" style="left:17px;top:282px">@TKBarlowOnline</div>
  </section>

  <!-- Card 6 -->
  <section class="card pink" style="left:343px;top:403px">
    <div class="line cond c-white" style="top:14px;font-size:32px">THAT STUBBORN</div>
    <div class="line cond c-white" style="top:46px;font-size:32px">WEIGHT?</div>
    <div class="line cond c-white" style="top:83px;font-size:19px;font-weight:500">IT'S NOT YOUR FAULT</div>
    <div class="photo" role="img" aria-label="Photo of TK in a black striped top, pointing down with both hands" style="left:44px;top:114px;width:160px;height:150px"></div>
    <div class="line script" style="top:220px;font-size:18px">Your hormones are to blame and</div>
    <div class="line script" style="top:237px;font-size:18px">you're not alone</div>
    <div class="line heavy c-yellow" style="top:262px;font-size:21px">BUT THERE IS A FIX</div>
    <div class="line handle c-white" style="top:290px">@TKBarlowOnline</div>
  </section>

  <!-- Card 7 -->
  <section class="card" style="left:614px;top:403px">
    <div class="pink" style="left:0;top:0;width:248px;height:231px"></div>
    <div class="photo" role="img" aria-label="Photo of TK smiling in a black top and jeans, hand on hip" style="left:153px;top:76px;width:95px;height:155px"></div>
    <div class="heavy c-white" style="left:11px;top:20px;font-size:26px;font-weight:900;line-height:1">YOUR BELLY</div>
    <div class="heavy c-white" style="left:11px;top:48px;font-size:26px;font-weight:900;line-height:1">IS N'T FAT...</div>
    <div style="left:0;top:84px;width:160px;height:32px;background:var(--white)"></div>
    <div class="cond c-pink" style="left:11px;top:83px;font-size:27px;line-height:1.1">it's hormonal</div>
    <div class="heavy c-white" style="left:11px;top:135px;font-size:18px;line-height:1">AND HERE'S</div>
    <div class="heavy c-white" style="left:11px;top:153px;font-size:18px;line-height:1">HOW TO FIX IT</div>
    <div class="heavy c-white" style="left:11px;top:198px;font-size:17px;line-height:1">COMMENT</div>
    <div style="left:0;top:218px;width:152px;height:25px;background:var(--pink);border-radius:0 0 5px 0"></div>
    <div class="heavy c-yellow" style="left:11px;top:221px;font-size:21px;line-height:1">HORMONES</div>
    <div class="heavy c-ink" style="left:11px;top:251px;font-size:16px;line-height:1;white-space:nowrap">IF NOTHING IS WORKING</div>
    <div class="handle c-ink" style="left:11px;top:280px">@TKBarlowOnline</div>
  </section>

  <!-- Card 8 -->
  <section class="card pink" style="left:884px;top:403px">
    <div class="photo" role="img" aria-label="Photo of TK in a white cropped sweater, pointing upward" style="left:108px;top:100px;width:140px;height:148px"></div>
    <div class="cond c-white" style="left:14px;top:16px;font-size:23px;line-height:1">THE STUBBORN</div>
    <div class="cond c-yellow" style="left:14px;top:40px;font-size:48px;line-height:1">BELLY FAT</div>
    <div class="cond c-white" style="left:14px;top:97px;font-size:23px;line-height:1">AFTER 40?</div>
    <div class="heavy c-white" style="left:14px;top:132px;font-size:14px;line-height:1.15">IT'S NOT<br>ABOUT<br>CALORIES</div>
    <div class="heavy c-white" style="left:14px;top:192px;font-size:14px;line-height:1.15">IT'S ABOUT<br>YOUR<br>HORMONES</div>
    <div style="left:0;top:248px;width:248px;height:30px;background:var(--white)"></div>
    <div class="line heavy c-ink" style="top:253px;font-size:20px">HERE IS THE FIX!</div>
    <div class="line handle c-white" style="top:290px">@TKBarlowOnline</div>
  </section>

</main>
</body>
</html>
```